Need to drive pregnant women to my 3d4d ultrasound studio where i provide 4d ultrasound with hyperalistic imaging and gender reveals

Industry/Entity Type

Healthcare

Font styles to use
Decorative
Script

Requirements
Must have
• My Company name Latido de Luna 4D. EVERYTHING HAS TO BE IN SPANISH
Nice to have
• SIMPLE AND NOT TOO BUSY
Should not have
• website

```html
<!DOCTYPE html>
<html lang="es">
<head>
<meta charset="utf-8">
<title>Latido de Luna 4D – Banner</title>
<link rel="stylesheet" href="https://fonts.googleapis.com/css2?family=Roboto:wght@700&family=Dancing+Script:wght@700&display=swap">
<style>
  :root {
    --stage: #a0a0a0;
    --ink: #000000;
    --paper: #ffffff;
    --sheen: #5c5c5f;
    --scan-light: #c0671f;
    --scan-dark: #3b1a06;
    --skin-light: #efc3b3;
    --skin-dark: #b9806f;
  }
  * { margin: 0; padding: 0; box-sizing: border-box; }
  html, body {
    width: 1200px;
    height: 600px;
    overflow: hidden;
    background: var(--stage);
    font-family: "Roboto", Arial, sans-serif;
  }
  .banner {
    position: absolute;
    left: 78px;
    top: 154px;
    width: 1044px;
    height: 304px;
    overflow: hidden;
    background: var(--ink);
  }
  .banner__shapes {
    position: absolute;
    inset: 0;
    width: 100%;
    height: 100%;
  }
  .banner__title {
    position: absolute;
    left: 64px;
    top: 42px;
    color: var(--paper);
    font-family: "Roboto", Arial, sans-serif;
    font-weight: 700;
    font-size: 58px;
    line-height: 60px;
    letter-spacing: 0.3px;
    text-transform: uppercase;
  }
  .banner__tagline {
    position: absolute;
    left: 64px;
    top: 202px;
    width: 470px;
    color: var(--ink);
    font-family: "Dancing Script", "Brush Script MT", cursive;
    font-weight: 700;
    font-size: 29px;
    line-height: 38px;
    white-space: nowrap;
  }
  .gallery {
    position: absolute;
    left: 634px;
    top: 25px;
    width: 378px;
    height: 250px;
    background: var(--paper);
  }
  .gallery__photo {
    position: absolute;
    top: 5px;
    width: 182px;
    height: 240px;
  }
  .gallery__photo--scan {
    left: 5px;
    background: radial-gradient(ellipse at 45% 50%, var(--scan-light) 0%, #8a4410 55%, var(--scan-dark) 100%);
  }
  .gallery__photo--newborn {
    left: 192px;
    background: radial-gradient(ellipse at 45% 55%, var(--skin-light) 0%, #d9a08f 60%, var(--skin-dark) 100%);
  }
</style>
</head>
<body>
  <section class="banner">
    <svg class="banner__shapes" viewBox="0 0 1740 507" preserveAspectRatio="none" aria-hidden="true">
      <defs>
        <linearGradient id="headerSheen" x1="0" y1="0" x2="1" y2="0">
          <stop offset="0" stop-color="#000000"/>
          <stop offset="0.18" stop-color="#000000"/>
          <stop offset="0.4" stop-color="#5c5c5f"/>
          <stop offset="0.72" stop-color="#000000"/>
          <stop offset="1" stop-color="#000000"/>
        </linearGradient>
      </defs>
      <polygon class="header-band" points="0,0 920,0 1137,302 0,302" fill="url(#headerSheen)"/>
      <polygon class="diagonal-stripe" points="920,0 1514,0 1894,507 1274,507" fill="#ffffff"/>
      <polygon class="tagline-band" points="0,302 889,302 1044,507 0,507" fill="#ffffff"/>
    </svg>

    <h1 class="banner__title">Latido de Luna<br>4D</h1>
    <p class="banner__tagline">Ecografías 4D con imágenes hiperrealistas<br>y revelación de género</p>

    <div class="gallery">
      <div class="gallery__photo gallery__photo--scan" role="img" aria-label="Imagen de ecografía 4D de un bebé en el vientre, en tonos ámbar"></div>
      <div class="gallery__photo gallery__photo--newborn" role="img" aria-label="Fotografía de un recién nacido dormido"></div>
    </div>
  </section>
</body>
</html>
```